VoxMend needs a Letterhead

We need a letterhead for our company "VoxMend Consultants". Logo is attached. The company color is Turquoise. Icons for website, scan logo for website, icons for address, e-mail and phone appreciated rather than just words.

Industry/Entity Type

It Company

```html
<!DOCTYPE html>
<html lang="en">
<head>
<meta charset="utf-8">
<title>VoxMend Consultants – Letterhead</title>
<link rel="stylesheet" href="https://fonts.googleapis.com/css2?family=Open+Sans:wght@400;600&display=swap">
<style>
  :root {
    --backdrop: #4f4f4f;
    --paper: #ffffff;
    --brand-blue: #1177c0;
    --brand-green: #8cc63f;
    --ink: #2b2b2b;
    --rule: #9a9a9a;
  }
  * { box-sizing: border-box; margin: 0; padding: 0; }
  html, body {
    width: 1200px; height: 1000px; overflow: hidden;
    background: var(--backdrop);
    font-family: "Open Sans", Arial, sans-serif;
  }
  .letterhead {
    position: absolute; left: 281px; top: 50px;
    width: 637px; height: 900px;
    background: var(--paper);
    box-shadow: 0 4px 14px rgba(0,0,0,.35);
    overflow: hidden;
  }
  .letterhead__swoosh {
    position: absolute; left: 0; width: 637px; height: 52px;
  }
  .letterhead__swoosh--top { top: 0; }
  .letterhead__swoosh--bottom { bottom: 0; }
  .brand {
    position: absolute; left: 372px; top: 34px;
    display: flex; align-items: center; gap: 10px;
    color: var(--brand-blue); font-weight: 600;
  }
  .brand__mark {
    width: 40px; height: 40px; background: var(--brand-blue);
  }
  .brand__name { font-size: 26px; line-height: 1; }
  .brand__tag { display: block; font-size: 10px; letter-spacing: 3px; margin-top: 4px; }
  .contact {
    position: absolute; left: 47px; top: 830px;
    display: flex; gap: 10px;
    font-size: 8px; color: var(--ink);
  }
  .contact__col { display: flex; flex-direction: column; gap: 2px; }
  .contact__col + .contact__col {
    border-left: 1px solid var(--rule); padding-left: 10px;
  }
  .contact__item { display: flex; align-items: center; gap: 5px; line-height: 10px; }
  .contact__icon { width: 9px; height: 9px; flex: none; }
</style>
</head>
<body>
  <main class="letterhead">
    <svg class="letterhead__swoosh letterhead__swoosh--top" viewBox="0 0 637 52" preserveAspectRatio="none" aria-hidden="true">
      <path d="M0 0 H637 V24 Q320 12 0 27 Z" fill="var(--brand-blue)"/>
      <path d="M0 33 Q170 16 405 14 Q170 24 0 46 Z" fill="var(--brand-green)"/>
    </svg>

    <div class="brand">
      <span class="brand__mark"></span>
      <div>
        <span class="brand__name">VoxMend</span>
        <span class="brand__tag">CONSULTANTS</span>
      </div>
    </div>

    <footer class="contact">
      <div class="contact__col">
        <span class="contact__item">
          <svg class="contact__icon" viewBox="0 0 10 10"><rect width="10" height="10" rx="2" fill="var(--brand-blue)"/><path d="M3 2 L4.5 3.5 L3.8 4.4 Q4.6 5.8 5.6 6.2 L6.5 5.5 L8 7 L7 8 Q3.5 7.5 2 3 Z" fill="#fff"/></svg>
          08 5510 2934
        </span>
        <span class="contact__item">
          <svg class="contact__icon" viewBox="0 0 10 10"><rect width="10" height="10" rx="2" fill="var(--brand-blue)"/><rect x="2" y="4" width="6" height="4" fill="#fff"/><rect x="3" y="2" width="4" height="2" fill="#fff"/></svg>
          08 5510 2935
        </span>
        <span class="contact__item">
          <svg class="contact__icon" viewBox="0 0 10 10"><rect width="10" height="10" rx="2" fill="var(--brand-blue)"/><rect x="2" y="3" width="6" height="4.5" fill="#fff"/><path d="M2 3 L5 5.5 L8 3" stroke="var(--brand-blue)" stroke-width=".8" fill="none"/></svg>
          hello@voxmend.com
        </span>
      </div>
      <div class="contact__col">
        <span class="contact__item">
          <svg class="contact__icon" viewBox="0 0 10 10"><rect width="10" height="10" rx="2" fill="var(--brand-blue)"/><circle cx="5" cy="5" r="3" stroke="#fff" stroke-width=".8" fill="none"/><path d="M2 5 H8 M5 2 V8" stroke="#fff" stroke-width=".6"/></svg>
          www.voxmend.com
        </span>
        <span class="contact__item">
          <svg class="contact__icon" viewBox="0 0 10 10"><rect width="10" height="10" rx="2" fill="var(--brand-blue)"/><path d="M5 8.5 L2.8 5 A2.5 2.5 0 1 1 7.2 5 Z" fill="#fff"/><circle cx="5" cy="4" r=".9" fill="var(--brand-blue)"/></svg>
          48 Ferndale Road - Brookton Po Box 5120
        </span>
      </div>
    </footer>

    <svg class="letterhead__swoosh letterhead__swoosh--bottom" viewBox="0 0 637 52" preserveAspectRatio="none" aria-hidden="true">
      <path d="M0 22 Q170 32 405 35 Q170 38 0 36 Z" fill="var(--brand-green)"/>
      <path d="M0 39 Q320 38 637 33 V52 H0 Z" fill="var(--brand-blue)"/>
    </svg>
  </main>
</body>
</html>
```